Healthcare IT firm needs classy and unique business care design

We need a business card design that incorporates our new logo design (attached) Prefer a purple based designed. I would really love to see something utilizing the "3D" version of the logo (purple on the reflective wall). I want something a little more than my logo printed along with a person's detailed contact information.
Contact Information for Business Card
Want something polished, professional, and a little unique in the design.
Colors
6b449b
Requirements
Must have
- Please use similar font as the logo design
Nice to have
- Would like to see the 3d version of my logo incorporated into the design.

```html
<!DOCTYPE html>
<html lang="en">
<head>
<meta charset="utf-8">
<title>Veranta Business Card</title>
<link href="https://fonts.googleapis.com/css2?family=Roboto:wght@400;500;700&display=swap" rel="stylesheet">
<style>
  :root {
    --backdrop: #2f2925;
    --card-purple: #4b3270;
    --card-purple-deep: #432c65;
    --ink-white: #ffffff;
    --ink-muted: #b9b1c6;
    --foil: #d9d6de;
  }
  html, body {
    margin: 0;
    padding: 0;
    width: 1200px;
    height: 769px;
    overflow: hidden;
    background: var(--backdrop);
    font-family: "Roboto", Arial, sans-serif;
  }
  .stage {
    position: relative;
    width: 1200px;
    height: 769px;
  }
  .card {
    position: absolute;
    top: 236px;
    width: 520px;
    height: 297px;
    background: linear-gradient(160deg, var(--card-purple) 0%, var(--card-purple-deep) 100%);
    box-shadow: 0 14px 30px rgba(0,0,0,0.45);
  }
  .card-front { left: 50px; }
  .card-back { left: 630px; }

  /* Front */
  .front-brand {
    position: absolute;
    left: 0; right: 0;
    top: 108px;
    text-align: center;
    color: var(--foil);
    font-weight: 700;
    font-size: 58px;
    letter-spacing: -1px;
    line-height: 1;
  }
  .front-tagline {
    position: absolute;
    left: 0; right: 0;
    top: 174px;
    text-align: center;
    color: var(--foil);
    font-weight: 500;
    font-size: 13px;
    letter-spacing: 2px;
  }

  /* Back */
  .back-frame {
    position: absolute;
    left: 18px; top: 18px; right: 18px; bottom: 22px;
    border: 2px solid var(--ink-white);
  }
  .back-tagline {
    position: absolute;
    left: 112px;
    bottom: 12px;
    padding: 0 10px;
    background: var(--card-purple-deep);
    color: var(--ink-white);
    font-weight: 500;
    font-size: 17px;
    letter-spacing: 1px;
    line-height: 20px;
  }
  .contact-block {
    position: absolute;
    left: 150px;
    top: 66px;
    color: var(--ink-white);
  }
  .back-brand {
    margin: 0 0 2px 88px;
    font-weight: 700;
    font-size: 36px;
    letter-spacing: -0.5px;
    line-height: 1.05;
  }
  .person {
    margin: 0 0 4px 40px;
    font-weight: 700;
    font-size: 20px;
  }
  .person .role {
    color: var(--ink-muted);
    font-weight: 400;
    font-size: 15px;
  }
  .details {
    margin: 0;
    font-size: 12.5px;
    line-height: 1.5;
  }
</style>
</head>
<body>
<main class="stage">
  <section class="card card-front" aria-label="Card front">
    <div class="front-brand">Veranta</div>
    <div class="front-tagline">HEALTHCARE SOLUTIONS</div>
  </section>

  <section class="card card-back" aria-label="Card back">
    <div class="back-frame"></div>
    <div class="back-tagline">HEALTHCARE SOLUTIONS</div>
    <div class="contact-block">
      <h1 class="back-brand">Veranta</h1>
      <p class="person">Daniel Reyes - <span class="role">CEO/Founder</span></p>
      <p class="details">
        2140 Willow Crest Road, Juneau, Alaska 99801<br>
        P. 555 214 7730 M. 555 318 4426 F. 555 902 6158<br>
        E. hello@veranta.com W. www.veranta.com
      </p>
    </div>
  </section>
</main>
</body>
</html>
```